Cleaning service website design

We need a new nice web design(logo will be the same) for a new cleaning service Company:

Informations about Company and logo you can take from flyers in attachments.

This is a cleaning service Company which have simple rules and we would like to show that(in checklist form) on website:

- What we do and that we're Cleaning Green

- Why us?

- How much(our pricing is simple)

Also we would like to communicate with clients by some nice/big pictures on website and the most important thing is our phone number and short/fast Freestimate.

Also there should be some space for description about our Company.

Generally all information on main page can be short: about us, about service(what we do), last reviews, tips (for example: Tip of the week) and other can be some introduction to subpage where will be more information.

There will be few subpages like: About us, About our service, Photos(Before and after), Reviews , Tips, FAQ, Contact, Looking for a Job? - most of them will be just text so you can project just one example.

```html
<!DOCTYPE html>
<html lang="en">
<head>
<meta charset="utf-8">
<title>Tidy Nest House Cleaning</title>
<link rel="stylesheet" href="https://fonts.googleapis.com/css2?family=Open+Sans:wght@300;400;600&family=PT+Sans:wght@400;700&display=swap">
<style>
:root{
  --green:#5fb14f;
  --green-light:#7cc56a;
  --green-text:#8cbf3f;
  --blue:#1f5fa8;
  --ink:#3a3a3a;
  --muted:#555;
  --page:#f2f2f2;
  --bar:#e6e6e6;
  --dark:#2b2b2b;
  --darker:#1e1e1e;
  --white:#fff;
}
*{margin:0;padding:0;box-sizing:border-box}
html,body{width:679px;height:1200px;overflow:hidden}
body{position:relative;background:var(--page);font-family:"Open Sans",Arial,sans-serif;color:var(--ink)}
.abs{position:absolute}
ul{list-style:none}

/* header */
.site-header{left:0;top:0;width:679px;height:66px;background:linear-gradient(#fafafa,#ececec);border-top:3px solid var(--green)}
.brand{left:88px;top:12px;display:flex;align-items:center;gap:6px}
.brand-dot{width:14px;height:14px;border-radius:50%;background:var(--blue)}
.brand-name{font-family:"PT Sans",sans-serif;font-weight:700;font-size:20px;color:var(--green)}
.brand-sub{left:115px;top:44px;font-size:8px;color:var(--blue)}
.main-nav{left:252px;top:0;display:flex;height:42px}
.main-nav a{font-family:"PT Sans",sans-serif;font-size:7.5px;color:#333;text-decoration:none;padding:0 8px;line-height:42px;letter-spacing:.2px}
.main-nav a.active{background:var(--green);color:var(--white)}

/* hero */
.hero{left:0;top:66px;width:679px;height:287px;background:linear-gradient(90deg,#e9e9e9,#f6f6f6 40%,#ececec);border-bottom:3px solid #ddd}
.hero-photo{left:88px;top:31px;width:327px;height:256px;background:linear-gradient(135deg,#d6e7cf,#c9ced8 55%,#f0c27a);border-radius:4px 4px 0 0}
.hero-arrow{top:138px;width:26px;height:26px;border-radius:50%;background:#222;display:flex;align-items:center;justify-content:center}
.tagline{left:348px;top:50px;width:241px;height:75px;background:var(--green);color:var(--white);font-family:"PT Sans",sans-serif;padding:2px 8px}
.tagline .l1{font-size:29px;line-height:32px}
.tagline .l2{font-size:19px;padding-left:30px;line-height:20px}
.tagline .l3{font-size:26px;text-align:right;line-height:22px}
.hero-phone{left:414px;top:168px;width:177px;height:36px;background:var(--blue);color:var(--white);padding:4px 10px 0;font-family:"PT Sans",sans-serif}
.hero-phone b{display:block;font-size:17px;font-weight:400;line-height:18px}
.hero-phone span{display:block;font-size:8px;line-height:10px}
.call-btn{left:472px;top:208px;width:119px;height:33px;border-radius:4px;background:linear-gradient(#7ecd6c,#4ea63e);color:var(--white);font-family:"PT Sans",sans-serif;font-size:17px;text-align:center;line-height:32px;box-shadow:0 2px 0 #3c8a30}

/* features */
.feature{top:366px;width:170px;text-align:center}
.feature .icon{display:block;width:44px;height:44px;margin:0 auto}
.feature h2{font-weight:400;font-size:11px;margin:8px 0 7px;color:#444}
.feature ul{text-align:left;font-size:6.8px;line-height:10.5px;color:#333;display:inline-block}
.feature li{padding-left:11px;position:relative}
.feature li::before{content:"\2714";position:absolute;left:0;font-size:6.5px}
.feature .note{text-align:center;font-size:6.8px;line-height:10.5px}
.read-more{font-size:7px;font-style:italic;color:var(--green-text);letter-spacing:.3px;text-transform:uppercase}
.feature .read-more{display:block;margin-top:3px}

/* section bars */
.section-bar{height:32px;background:var(--bar);font-family:"PT Sans",sans-serif;font-weight:400;font-size:14px;color:#333;padding-left:12px;line-height:32px}
.tips-bar{left:87px;top:530px;width:504px;font-size:12px;letter-spacing:.5px}

/* tips */
.tips-intro{left:87px;top:578px;width:118px;font-size:7px;line-height:10.5px}
.tips-intro .read-more{display:block;margin-top:12px}
.tip-card{top:578px;width:115px;height:141px;background:#e3e3e3;border:1px solid #ddd}
.tip-card .ph{width:113px;height:115px}
.tip-card p{font-variant:small-caps;font-size:8.5px;text-align:center;line-height:25px;letter-spacing:.5px;color:#444}

/* about */
.about-bar{left:87px;top:736px;width:332px}
.testi-bar{left:430px;top:736px;width:161px}
.testi-arrows{right:6px;top:10px;display:flex;gap:1px}
.testi-arrows i{width:12px;height:12px;background:#999;border-radius:2px}
.about-menu{left:87px;top:777px;width:77px}
.about-menu li{font-variant:small-caps;font-size:8px;border-bottom:1px solid #ddd;height:21px;line-height:20px;display:flex;justify-content:space-between;align-items:center;color:#444}
.about-menu li.active{color:var(--green-text)}
.about-menu li i{width:8px;height:8px;border-radius:50%;background:#888}
.about-menu li.active i{background:var(--blue)}
.about-text{left:172px;top:781px;width:240px;font-size:7px;line-height:10.6px}
.about-text p+p{margin-top:10px}
.quote{left:430px;top:784px;width:161px;height:66px;background:#e6e6e6;padding:7px 10px 0 24px;font-size:6.2px;font-style:italic;line-height:8px;color:#555}
.quote .q{position:absolute;left:9px;top:4px;font-size:16px;color:#777;font-style:normal}
.quote .lead{font-size:6.8px;margin-bottom:4px}
.quote-tail{left:571px;top:850px;width:0;height:0;border-left:6px solid transparent;border-right:6px solid transparent;border-top:6px solid #e6e6e6}
.quote-by{left:484px;top:872px;font-size:6.8px;font-style:italic;color:var(--blue)}
.avatar{left:555px;top:864px;width:32px;height:25px;border:2px solid #fff;box-shadow:0 0 0 1px #aaa;background:linear-gradient(#8fb0d6,#5b4a3e)}

/* promo cards */
.promo{top:907px;width:160px}
.promo .ph{height:100px;border:3px solid #e2e2e2;border-radius:3px}
.promo h3{font-variant:small-caps;font-weight:400;font-size:10.5px;margin:13px 0 6px;letter-spacing:.3px}
.promo p,.promo li{font-size:7px;line-height:10.5px}
.promo li{padding-left:11px;position:relative}
.promo li::before{content:"\2714";position:absolute;left:0;font-size:6.5px}
.promo .read-more{display:block;text-align:center;margin-top:7px}
.estimate{background:var(--green-light);position:relative}
.estimate span{position:absolute;right:8px;top:40px;color:var(--white);font-family:"PT Sans",sans-serif;text-align:left;font-size:14px;line-height:18px}

/* footer */
.site-footer{left:0;top:1102px;width:679px;height:65px;background:linear-gradient(#353535,var(--dark))}
.footer-notch{left:332px;top:1102px;border-left:9px solid transparent;border-right:9px solid transparent;border-top:8px solid var(--page)}
.site-footer h4{position:absolute;left:87px;top:16px;font-weight:400;font-size:10.5px;color:var(--white);letter-spacing:.3px}
.site-footer .blurb{position:absolute;left:87px;top:35px;width:180px;font-size:7px;line-height:10px;color:#aaa}
.contact-line{position:absolute;left:289px;display:flex;align-items:center;gap:5px;font-size:6.5px;color:#ddd}
.copyright-bar{left:0;top:1167px;width:679px;height:33px;background:var(--darker);border-top:1px solid #444}
.copyright-bar p{position:absolute;left:87px;top:11px;font-size:7px;color:#ccc}
.social{position:absolute;left:501px;top:5px;display:flex;gap:6px}
.social i{width:19px;height:19px;border-radius:50%;background:#d8d8d8;border:2px solid #888}
</style>
</head>
<body>

<header class="site-header abs">
  <div class="brand abs"><span class="brand-dot"></span><span class="brand-name">Tidy Nest</span></div>
  <div class="brand-sub abs">house cleaning</div>
  <nav class="main-nav abs">
    <a class="active">HOME</a><a>ABOUT US</a><a>SERVICES</a><a>GALLERY</a><a>TIPS</a><a>LOOKING FOR A JOB</a><a>FAQ</a><a>REVIEWS</a><a>CONTACT</a>
  </nav>
</header>

<section class="hero abs">
  <div class="hero-photo abs" role="img" aria-label="Two smiling cleaners holding a broom and a bucket of cleaning supplies"></div>
  <div class="hero-arrow abs" style="left:7px"><svg width="10" height="10" viewBox="0 0 10 10"><path d="M7 1L3 5l4 4" stroke="#fff" stroke-width="2" fill="none"/></svg></div>
  <div class="hero-arrow abs" style="left:642px"><svg width="10" height="10" viewBox="0 0 10 10"><path d="M3 1l4 4-4 4" stroke="#fff" stroke-width="2" fill="none"/></svg></div>
  <div class="tagline abs"><div class="l1">Affordably</div><div class="l2">making your life</div><div class="l3">Simpler</div></div>
  <div class="hero-phone abs"><b>555-014-2290</b><span>www.TidyNestClean.ca</span></div>
  <div class="call-btn abs">Call Today!</div>
</section>

<section class="feature abs" style="left:74px">
  <div class="icon" role="img" aria-label="Maid with vacuum icon" style="border-radius:6px;background:#666"></div>
  <h2>WHAT WE DO</h2>
  <ul>
    <li>Thoroughly clean your bathrooms,<br>kitchen, bedrooms and living areas</li>
    <li>Mop or vacuum your floors</li>
    <li>Dust surfaces</li>
    <li>Collect garbage</li>
    <li>Make beds</li>
  </ul>
  <span class="read-more">Read more &gt;</span>
</section>

<section class="feature abs" style="left:243px">
  <svg class="icon" viewBox="0 0 44 44"><circle cx="22" cy="22" r="19" fill="none" stroke="#555" stroke-width="3.5"/><text x="22" y="31" text-anchor="middle" font-family="Open Sans,sans-serif" font-size="26" font-weight="600" fill="#555">?</text></svg>
  <h2>WHY &nbsp;US</h2>
  <ul>
    <li>Locally Owned &amp; Operated</li>
    <li>Reliable &amp; Affordable</li>
    <li>All Supplies Provided</li>
    <li>Green Cleaning</li>
    <li>Pet Friendly</li>
    <li>No Contracts</li>
  </ul>
  <span class="read-more">Read more &gt;</span>
</section>

<section class="feature abs" style="left:424px">
  <svg class="icon" viewBox="0 0 44 44"><rect x="17" y="2" width="10" height="8" rx="2" fill="#555"/><ellipse cx="22" cy="28" rx="15" ry="15" fill="#555"/><text x="22" y="35" text-anchor="middle" font-family="Open Sans,sans-serif" font-size="18" fill="#fff">$</text></svg>
  <h2>HOW MUCH</h2>
  <ul>
    <li>$79 for homes less than 1000 sq ft</li>
    <li>$89 for homes 1000-1800 sq ft</li>
    <li>$99 for homes 1800-2600 sq ft</li>
  </ul>
  <p class="note">*If your home is larger than<br>2600 sq ft please call for a quote.<br>*rates are for regular service*</p>
  <span class="read-more">Read more &gt;</span>
</section>

<h2 class="section-bar tips-bar abs">TIPS OF THE WEEK</h2>
<div class="tips-intro abs">
  <p>We understand that reliability and thoroughness are what you look for in an affordable, professional house cleaning service. We pay attention to your needs. We get the job done!</p>
  <span class="read-more">Read more &gt;</span>
</div>
<figure class="tip-card abs" style="left:216px"><div class="ph" role="img" aria-label="Sweeping a wooden floor" style="background:linear-gradient(135deg,#e8d39a,#c98a44)"></div><p>Sweeping Solutions</p></figure>
<figure class="tip-card abs" style="left:346px"><div class="ph" role="img" aria-label="Woman wiping a kitchen counter" style="background:linear-gradient(135deg,#d9a24a,#4f6a8c)"></div><p>In The Kitchen</p></figure>
<figure class="tip-card abs" style="left:474px"><div class="ph" role="img" aria-label="Bathroom with a bathtub and fireplace" style="background:linear-gradient(135deg,#5a3d2a,#c9b9a6)"></div><p>Bathroom Boosters</p></figure>

<h2 class="section-bar about-bar abs">ABOUT</h2>
<h2 class="section-bar testi-bar abs">TESTIMONIALS<span class="testi-arrows abs"><i></i><i></i></span></h2>
<ul class="about-menu abs">
  <li class="active">About Us<i></i></li>
  <li>Mission<i></i></li>
  <li>Vision<i></i></li>
</ul>
<div class="about-text abs">
  <p>Have you ever wondered what it would be like if your life was simpler? We're here to help you get there by taking over the chore of house cleaning. With our help you'll have more time to spend on the things that matter most to you.</p>
  <p>With Tidy Nest you not only get a professional service, but you get it at an affordable price. The owner makes it apoint to be at each and every cleaning to assure your needs are met.</p>
</div>
<blockquote class="quote abs">
  <span class="q">&ldquo;</span>
  <p class="lead">It's about caring, not just cleaning.</p>
  <p>Having personally experienced the struggles of finding quality maid service for our home, we want to make it simpler for families in the Brookfield area.</p>
</blockquote>
<div class="quote-tail abs"></div>
<div class="quote-by abs">- Anna &amp; Peter</div>
<div class="avatar abs" role="img" aria-label="Portrait of the reviewers"></div>

<section class="promo abs" style="left:87px">
  <div class="ph" role="img" aria-label="Group of seniors walking on a golf course" style="background:linear-gradient(#c9d9b5,#7f9c5a)"></div>
  <h3>Rules</h3>
  <ul><li>Rule1- Lorem Ipsum is simply dummy</li><li>Rule2- Lorem Ipsum is simply dummy</li><li>Rule3- Lorem Ipsum is simply dummy</li></ul>
  <span class="read-more">Read more &gt;</span>
</section>
<section class="promo abs" style="left:258px">
  <div class="ph estimate" role="img" aria-label="Cleaner with a vacuum beside the free estimate offer"><span>SHORT &amp; FAST<br>FREE ESTIMATE</span></div>
  <h3>Short &amp; Fast Free Estimate</h3>
  <p>Lorem Ipsum is simply dummy text of the printing and typesetting industry. Lorem Ipsum has been the industry's standard</p>
  <span class="read-more">Read more &gt;</span>
</section>
<section class="promo abs" style="left:430px">
  <div class="ph" role="img" aria-label="Messy room before and tidy room after cleaning" style="background:linear-gradient(90deg,#8a6a4e 50%,#e6dccb 50%)"></div>
  <h3>Before &amp; After Reviews</h3>
  <p>Lorem Ipsum is simply dummy text of the printing and typesetting industry. Lorem Ipsum has been the industry's standard</p>
  <span class="read-more">Read more &gt;</span>
</section>

<footer class="site-footer abs">
  <h4>CONTACT INFO</h4>
  <p class="blurb">Lorem Ipsum is simply dummy text of the printing and typesetting industry.</p>
  <div class="contact-line" style="top:24px"><svg width="9" height="9" viewBox="0 0 10 10"><rect width="10" height="10" rx="2" fill="#ddd"/><path d="M3 2l1.5 2-1 1a5 5 0 002 2l1-1 2 1.5-1 1.5C5 9 1 5 1.5 3z" fill="#333"/></svg>PHONE : 555-014-2290</div>
  <div class="contact-line" style="top:42px"><svg width="9" height="9" viewBox="0 0 10 10"><rect y="1" width="10" height="8" fill="#ddd"/><path d="M0 1l5 4 5-4" stroke="#333" fill="none"/></svg>EMAIL &nbsp;: www.TidyNestClean.ca</div>
</footer>
<div class="footer-notch abs"></div>
<div class="copyright-bar abs">
  <p>Copyright &copy; 2013 TidyNestClean All Rights Reserved.</p>
  <div class="social"><i></i><i></i><i></i><i></i></div>
</div>

</body>
</html>
```